Kelvo Tech Oz Business card revamp

We are looking to revamp our business card design. We are hoping to change our colours to dark navey blue, gray, white and black but are open to keeping the same if a good design is submited. We are after somthing a bit differnt not just boring business card. I have attached a copy of our current card. We Want to keep the same logo design which i have attached a few to hopfully help you in this process. We are after a design that can be personalized to separate 4 people

Colors
0455a3
ffffff
000000
cbcbcb

Requirements
Must have
• Kelvo Tech Logo, address 3/41 Mallory Court, Wexhill 4218, phone number, Name and position

```html
<!DOCTYPE html>
<html lang="en">
<head>
<meta charset="utf-8">
<title>Kelvo Tech Oz – Business Card</title>
<link rel="stylesheet" href="https://fonts.googleapis.com/css2?family=Open+Sans:wght@400;600;700;800&display=swap">
<style>
  :root {
    --brand-blue: #2b7ec1;
    --brand-blue-deep: #1f6fb2;
    --brand-orange: #f07a22;
    --card-white: #ffffff;
    --backdrop: #4a4c4f;
    --card-shadow: rgba(0, 0, 0, 0.45);
  }
  * { box-sizing: border-box; margin: 0; padding: 0; }
  html, body { width: 1200px; height: 800px; overflow: hidden; }
  body {
    background: var(--backdrop);
    font-family: "Open Sans", Arial, sans-serif;
    display: flex;
    align-items: center;
    justify-content: center;
    gap: 60px;
  }
  .card {
    position: relative;
    width: 520px;
    height: 300px;
    background: var(--card-white);
    box-shadow: 0 14px 30px var(--card-shadow);
    overflow: hidden;
  }

  /* Front */
  .card-front .brand {
    position: absolute;
    left: 0; right: 0; top: 60px;
    text-align: center;
  }
  .brand-row {
    display: inline-flex;
    align-items: center;
    gap: 14px;
  }
  .brand-dot {
    width: 34px; height: 34px;
    border-radius: 50%;
    background: var(--brand-orange);
  }
  .brand-name {
    font-size: 54px;
    font-weight: 800;
    color: var(--brand-blue);
    line-height: 1;
    letter-spacing: -1px;
  }
  .brand-descriptor {
    margin-top: 6px;
    font-size: 20px;
    font-weight: 700;
    color: var(--brand-blue);
  }
  .card-front .tagline {
    position: absolute;
    left: 0; right: 0; top: 168px;
    text-align: center;
    font-size: 20px;
    font-weight: 600;
    color: var(--brand-blue);
  }
  .card-front .rule {
    position: absolute;
    left: 0; right: 0; top: 200px;
    height: 3px;
    background: var(--brand-blue);
  }
  .card-front .website {
    position: absolute;
    left: 0; right: 0; top: 212px;
    text-align: center;
    font-size: 16px;
    font-weight: 700;
    color: var(--brand-orange);
  }

  /* Back */
  .card-back .panel {
    position: absolute;
    inset: 0;
    width: 100%;
    height: 100%;
  }
  .card-back .contact {
    position: absolute;
    left: 34px; top: 44px;
    color: var(--card-white);
  }
  .person-name { font-size: 24px; font-weight: 700; line-height: 1.1; }
  .person-role { font-size: 15px; font-weight: 700; margin-top: 2px; }
  .phone {
    display: flex; align-items: center; gap: 10px;
    margin-top: 18px;
    font-size: 20px; font-weight: 600;
  }
  .phone svg { width: 24px; height: 24px; }
  .card-back .footer {
    position: absolute;
    left: 34px; bottom: 30px;
    color: var(--card-white);
  }
  .address { font-size: 12px; font-weight: 400; }
  .footer .website { font-size: 17px; font-weight: 700; margin-top: 6px; }
  .card-back .side-brand {
    position: absolute;
    right: 26px; top: 50%;
    transform: translate(50%, -50%) rotate(90deg);
    transform-origin: center;
    white-space: nowrap;
    text-align: center;
    margin-right: 22px;
  }
  .side-brand .brand-name { font-size: 34px; }
  .side-brand .brand-descriptor { font-size: 13px; margin-top: 2px; }
</style>
</head>
<body>

  <section class="card card-front" aria-label="Business card front">
    <div class="brand">
      <div class="brand-row">
        <span class="brand-dot"></span>
        <span class="brand-name">Kelvo Tech</span>
      </div>
      <div class="brand-descriptor">Passive Fire Protection</div>
    </div>
    <p class="tagline">Reliability with dedication to service</p>
    <div class="rule"></div>
    <p class="website">www.kelvotech.com.au</p>
  </section>

  <section class="card card-back" aria-label="Business card back">
    <svg class="panel" viewBox="0 0 520 300" preserveAspectRatio="none" aria-hidden="true">
      <path d="M0 0 H330 C300 90 340 200 390 300 H0 Z" fill="var(--brand-blue)"/>
    </svg>

    <div class="contact">
      <p class="person-name">Sam Carter</p>
      <p class="person-role">Designation</p>
      <p class="phone">
        <svg viewBox="0 0 24 24" aria-hidden="true">
          <rect x="2" y="3" width="20" height="18" rx="4" fill="var(--brand-orange)"/>
          <path d="M8 7c-1 0-2 1-1.6 2.4 1 3.4 3.6 6 7 7 1.4.4 2.4-.6 2.4-1.6l-2.2-1.4-1.2 1c-1.6-.8-2.6-1.8-3.4-3.4l1-1.2Z" fill="var(--card-white)"/>
        </svg>
        170-318 (2904)
      </p>
    </div>

    <div class="footer">
      <p class="address">3/41 Mallory Court, Wexhill 4218</p>
      <p class="website">www.kelvotech.com.au</p>
    </div>

    <div class="side-brand">
      <div class="brand-name">Kelvo Tech</div>
      <div class="brand-descriptor">Passive Fire Protection</div>
    </div>
  </section>

</body>
</html>
```